Boutique Financial Services/Advisor Business Needs Web Design

Looking for an informational and functional web design for my Financial Services/Financial Advisement business. It should have functionality for Company name, address, phone #, "About Us", Who we are, Our Mission, Services we offer, Biographies/Photos of/about "The Team", and possibly a link to "Contact Us". Would like to see something new & exciting blended with a traditional/professional look that will appeal to those approaching retirement, as well as those younger clients that are beginning to think about planning for the future. I already have a web domain through Brixwell, but would like this to be the design we use for that domain.
Financial Services/Financial Advisor
Coded - Design and coding required
1 page

```html
<!DOCTYPE html>
<html lang="en">
<head>
<meta charset="utf-8">
<title>Crestline Wealth Management</title>
<link href="https://fonts.googleapis.com/css2?family=Cinzel:wght@400;500&family=Montserrat:wght@400;500;600;700&display=swap" rel="stylesheet">
<style>
:root{
  --navy:#28285c;
  --navy-dark:#1f1f4d;
  --grey:#8d8d90;
  --grey-light:#e6e6e8;
  --grey-mid:#cfcfd2;
  --text:#3a3a4a;
  --white:#ffffff;
}
*{box-sizing:border-box;margin:0;padding:0}
html,body{width:1200px;height:4785px;overflow:hidden}
body{font-family:"Montserrat",sans-serif;color:var(--text);background:var(--white);position:relative}
section,header,footer{position:absolute;left:0;width:1200px;overflow:hidden}
.abs{position:absolute}
.serif{font-family:"Cinzel",serif;font-weight:400;color:var(--navy);letter-spacing:2px;white-space:nowrap}
.eyebrow{font-size:17px;font-weight:500;letter-spacing:1.5px;color:var(--navy)}
.photo{position:absolute}
.underline{position:absolute;height:4px;background:var(--navy)}

/* hero */
.hero{top:0;height:734px;background:linear-gradient(100deg,#eeeef0 0%,#e3e3e6 60%,#d9d9dc 100%)}
.hero-photo{left:540px;top:0;width:660px;height:734px;background:linear-gradient(90deg,rgba(227,227,230,1) 0%,rgba(214,196,178,.6) 25%,#c9b29b 50%,#a9a4a6 75%,#8fa0b7 100%)}
.topbar{left:0;top:0}
.topbar-info{position:absolute;top:12px;font-size:14px;color:var(--white);font-weight:500;display:flex;align-items:center;gap:10px;white-space:nowrap}
.logo{position:absolute;text-align:center;color:var(--navy);font-family:"Montserrat",sans-serif;font-weight:500;line-height:1.15;letter-spacing:1px;white-space:nowrap}
.nav{position:absolute;top:79px;left:383px;font-size:12px;font-weight:600;color:#2e2e3e;letter-spacing:.5px}
.nav a{color:inherit;text-decoration:none;position:absolute;white-space:nowrap}
.nav-btn{position:absolute;left:957px;top:71px;width:128px;height:33px;background:var(--grey);color:var(--white);font-size:11px;font-weight:600;display:flex;align-items:center;justify-content:center;gap:8px}
.hero h1{font-size:40px;line-height:52px;left:104px;top:272px}
.hero h1 .light{color:var(--grey)}
.hero-kicker{left:106px;top:240px;font-size:17px;font-weight:500;color:#2e2e3e;letter-spacing:.5px;white-space:nowrap}
.hero-kicker::after{content:"";display:inline-block;width:52px;height:2px;background:var(--grey);margin-left:8px;vertical-align:middle}
.hero-text{left:106px;top:385px;width:470px;font-size:15px;line-height:28px;color:#3a3a4a}
.btn{position:absolute;background:var(--grey);color:var(--white);font-weight:600;font-size:16px;letter-spacing:1px;display:flex;align-items:center;gap:18px;padding-left:4px;white-space:nowrap}
.btn.navy{background:var(--navy)}

.vline{position:absolute;width:2px;background:#b8b8bc}

/* about */
.about{top:767px;height:617px;background:var(--white)}
.value{position:absolute;left:641px;width:490px;display:flex;gap:22px}
.value h3{font-size:17px;font-weight:600;color:#2e2e3e;margin-bottom:2px}
.value p{font-size:16px;line-height:22px;color:#3a3a4a}
.divider{position:absolute;height:1px;background:#9a9aa0}

/* services */
.services{top:1436px;height:706px;background:linear-gradient(180deg,#e2e2e4,#d6d6d9)}
.services h2{width:1200px;text-align:center;font-size:38px}
.card{position:absolute;background:var(--white);box-shadow:0 2px 6px rgba(0,0,0,.12);text-align:center}
.card .photo{left:0;top:0;width:100%}
.card h3{font-size:19px;font-weight:500;color:#1f1f2e;position:absolute;width:100%}
.card p{position:absolute;left:26px;right:26px;font-size:12.5px;line-height:19px;color:#3a3a4a}
.diamond{position:absolute;width:62px;height:62px;transform:rotate(45deg);background:var(--grey)}

/* mission */
.mission{top:2142px;height:604px;background:#eef0ee}
.mission-box{left:115px;top:138px;width:504px;height:312px;background:var(--white)}
.mission h2{font-size:36px}
.mission-text{font-size:15px;line-height:24px;color:#3a3a4a}

/* team */
.team{top:2746px;height:989px;background:var(--white)}
.member{position:absolute;width:306px;height:320px;overflow:hidden}
.member .photo{left:0;top:0;width:100%;height:100%}
.member .frame{position:absolute;left:14px;top:14px;right:14px;bottom:14px;border:1px solid rgba(255,255,255,.45)}
.member .name{position:absolute;left:0;bottom:0;width:100%;height:60px;background:var(--navy);color:var(--white);font-size:21px;font-weight:600;display:flex;align-items:center;justify-content:center;letter-spacing:.5px}
.member .name::after{content:"";position:absolute;bottom:10px;left:50%;width:36px;height:2px;margin-left:-18px;background:var(--white)}
.member.active .photo{background:#6d6d72}
.member.active .overlay{position:absolute;left:14px;top:14px;right:14px;bottom:14px;border:1px solid rgba(255,255,255,.6);text-align:center;color:var(--white);padding:50px 30px 0}
.overlay h4{font-size:21px;font-weight:600;margin-bottom:14px}
.overlay p{font-size:12.5px;line-height:23px;color:#e5e5ea}
.overlay a{display:inline-block;margin-top:14px;font-size:12px;font-weight:600;color:var(--white);text-decoration:underline}

/* contact */
.contact{top:3735px;height:659px;background:linear-gradient(90deg,#b7b7ba 0%,#cdcdd0 45%,#e6e6e8 60%,#f0f0f0 100%)}
.contact h2{font-size:38px}
.field{position:absolute;background:var(--white);font-size:14px;color:#6a6a72;display:flex;align-items:center;gap:8px;padding-left:16px;border:1px solid #ddd}
.field.area{align-items:flex-start;padding-top:14px}

/* footer */
.footer{top:4394px;height:391px;background:var(--white)}
.footer h4{font-family:"Cinzel",serif;font-weight:400;font-size:21px;color:var(--navy);letter-spacing:1px;position:absolute;padding-bottom:8px;border-bottom:1px solid #9a9aa0;white-space:nowrap}
.footer ul{list-style:none;position:absolute;font-size:13px;color:#2e2e3e;font-weight:500}
.footer li{height:27px}
.fcontact{position:absolute;display:flex;gap:14px;font-size:13px;line-height:19px;color:#2e2e3e;font-weight:500;white-space:nowrap}
.icon-dot{width:26px;height:26px;border-radius:50%;background:var(--navy);flex:none;display:flex;align-items:center;justify-content:center}
.social{position:absolute;width:28px;height:28px;border-radius:50%;background:var(--navy)}
.copyright{position:absolute;left:0;width:1200px;top:325px;text-align:center;font-size:13px;color:#4a4a55}
.copyright u{color:var(--navy)}
</style>
</head>
<body>

<!-- HERO -->
<header class="hero">
  <div class="photo hero-photo" role="img" aria-label="Smiling couple shaking hands with an advisor across a desk with a laptop"></div>
  <svg class="abs topbar" width="1200" height="46" viewBox="0 0 1200 46"><polygon points="539,0 1200,0 1200,46 517,46" fill="#28285c"/></svg>
  <div class="topbar-info" style="left:560px">
    <svg width="22" height="22" viewBox="0 0 22 22"><circle cx="11" cy="11" r="11" fill="#fff"/><path d="M11 5a4 4 0 0 0-4 4c0 3 4 8 4 8s4-5 4-8a4 4 0 0 0-4-4z" fill="#28285c"/><circle cx="11" cy="9" r="1.5" fill="#fff"/></svg>
    27 Harbor Lane, Fairview, NY
  </div>
  <div class="topbar-info" style="left:900px;font-size:16px">
    <svg width="22" height="22" viewBox="0 0 22 22"><circle cx="11" cy="11" r="11" fill="#fff"/><path d="M7 6l3 0 1 3-2 1a7 7 0 0 0 3 3l1-2 3 1 0 3c-6 0-9-3-9-9z" fill="#28285c"/></svg>
    (+123) 555 0148
  </div>
  <div class="logo" style="left:82px;top:76px;width:250px">
    <div style="font-size:21px">CRESTLINE WEALTH</div>
    <div style="font-size:17px;letter-spacing:4px">MANAGEMENT</div>
  </div>
  <nav class="nav">
    <a style="left:0">ABOUT US</a>
    <a style="left:111px">WHO WE ARE</a>
    <a style="left:247px">MISSION</a>
    <a style="left:338px">SERVICES</a>
    <a style="left:451px">THE TEAM</a>
  </nav>
  <div class="nav-btn">
    <svg width="18" height="18" viewBox="0 0 18 18"><path d="M2 2l8 7-8 7M7 2l8 7-8 7" fill="none" stroke="#fff" stroke-width="1.5"/></svg>
    CONTACT US
  </div>
  <div class="abs hero-kicker">CRESTLINE WEALTH MANAGEMENT</div>
  <h1 class="abs serif">GUIDING YOU TO YOUR<br><span class="light">FINANCIAL SUMMIT</span></h1>
  <p class="abs hero-text">Lorem ipsum dolor sit amet, consectetur adipiscing elit, sed do eiusmod tempor incididunt ut labore.</p>
  <div class="btn" style="left:108px;top:465px;width:180px;height:44px">
    <svg width="32" height="36" viewBox="0 0 32 36"><path d="M3 3l22 15L3 33M10 10l12 8-12 8" fill="none" stroke="#fff" stroke-width="2"/></svg>
    CONTACT US
  </div>
</header>
<div class="vline" style="left:600px;top:734px;height:33px"></div>

<!-- ABOUT -->
<section class="about">
  <svg class="abs" style="left:0;top:0" width="502" height="617" viewBox="0 0 502 617"><polygon points="0,0 502,0 223,617 0,617" fill="#28285c"/></svg>
  <svg class="abs" style="left:80px;top:69px" width="490" height="490" viewBox="0 0 490 490">
    <circle cx="245" cy="245" r="240" fill="#9c9ca0"/>
    <defs><linearGradient id="aboutPhoto" x1="0" y1="0" x2="1" y2="1"><stop offset="0" stop-color="#e6e0d8"/><stop offset=".5" stop-color="#cdbfae"/><stop offset="1" stop-color="#8fa4b8"/></linearGradient></defs>
    <circle cx="245" cy="245" r="222" fill="url(#aboutPhoto)" role="img" aria-label="Senior couple reviewing documents with an advisor at a laptop"/>
  </svg>
  <div class="abs eyebrow" style="left:626px;top:70px">OUR VALUES</div>
  <h2 class="abs serif" style="left:624px;top:93px;font-size:40px">ABOUT COMPANY</h2>
  <div class="underline" style="left:626px;top:147px;width:76px"></div>
  <p class="abs" style="left:626px;top:173px;width:500px;font-size:16px;line-height:23px">Lorem ipsum dolor sit amet, consectetur adipiscing elit, sed do eiusmod tempor incididunt ut labore et</p>
  <div class="value" style="top:257px">
    <svg width="56" height="50" viewBox="0 0 56 50" fill="none" stroke="#28285c" stroke-width="2"><path d="M2 18l10-6 10 4 8-4 12 2 12 6M8 22l14 14 4-2 4 2 4-2 8-6M22 16l-6 8 4 2 8-6"/></svg>
    <div><h3>Integrity</h3><p>Lorem ipsum dolor sit amet, consectetur adip-<br>iscing elit, sed do eiusmod tempor</p></div>
  </div>
  <div class="divider" style="left:645px;top:347px;width:479px"></div>
  <div class="value" style="top:364px">
    <svg width="56" height="50" viewBox="0 0 56 50" fill="none" stroke="#28285c" stroke-width="2"><circle cx="28" cy="26" r="11"/><circle cx="28" cy="26" r="4"/><path d="M28 6v6M28 40v6M8 26h6M42 26h6M6 4h4M46 4h4"/></svg>
    <div><h3>Transparency</h3><p>Lorem ipsum dolor sit amet, consectetur adip-<br>iscing elit, sed do eiusmod tempor</p></div>
  </div>
  <div class="divider" style="left:645px;top:453px;width:479px"></div>
  <div class="value" style="top:471px">
    <svg width="56" height="52" viewBox="0 0 56 52" fill="none" stroke="#28285c" stroke-width="2"><circle cx="28" cy="10" r="6"/><circle cx="10" cy="22" r="4"/><circle cx="46" cy="22" r="4"/><path d="M18 48V26a10 10 0 0 1 20 0v22M2 48V34a8 8 0 0 1 14 0M40 34a8 8 0 0 1 14 0v14"/></svg>
    <div><h3>Professionalism</h3><p>Lorem ipsum dolor sit amet, consectetur adip-<br>iscing elit, sed do eiusmod tempor</p></div>
  </div>
</section>
<div class="vline" style="left:605px;top:1397px;height:71px;z-index:2"></div>

<!-- SERVICES -->
<section class="services">
  <div class="abs eyebrow" style="width:1200px;text-align:center;top:56px;color:#2e2e3e">WHAT WE DO</div>
  <h2 class="abs serif" style="top:82px">SERVICES WE <span style="color:var(--grey)">PROVIDE</span></h2>
  <div class="underline" style="left:576px;top:134px;width:64px"></div>

  <div class="card" style="left:132px;top:195px;width:295px;height:379px">
    <div class="photo" style="height:204px;background:linear-gradient(120deg,#e3ddd5,#c6b7a6 55%,#9aa8b6)" role="img" aria-label="Couple meeting with an advisor at a table"></div>
    <div class="diamond" style="left:116px;top:173px"></div>
    <h3 style="top:265px">Service heading</h3>
    <p style="top:295px">Lorem ipsum dolor sit amet, consecte-tur adipiscing elit, sed do eiusmod dipiscing elit, sed do eiusmod</p>
  </div>
  <div class="card" style="left:446px;top:180px;width:310px;height:422px;border-bottom:4px solid #9a9aa0">
    <div class="photo" style="height:218px;background:linear-gradient(120deg,#d8dbe0,#bdb3a8 50%,#8d98a8)" role="img" aria-label="Team of advisors shaking hands with a client"></div>
    <div class="diamond" style="left:124px;top:187px;background:var(--navy)"></div>
    <h3 style="top:283px">Service heading</h3>
    <p style="top:313px">Lorem ipsum dolor sit amet, consecte-tur adipiscing elit, sed do eiusmod dipiscing elit, sed do eiusmod</p>
  </div>
  <div class="card" style="left:773px;top:203px;width:295px;height:377px">
    <div class="photo" style="height:204px;background:linear-gradient(120deg,#e6e3de,#c9b5a0 55%,#a48a72)" role="img" aria-label="Smiling senior couple sitting together at home"></div>
    <div class="diamond" style="left:116px;top:173px"></div>
    <h3 style="top:265px">Service heading</h3>
    <p style="top:295px">Lorem ipsum dolor sit amet, consecte-tur adipiscing elit, sed do eiusmod dipiscing elit, sed do eiusmod</p>
  </div>
</section>
<div class="vline" style="left:605px;top:2103px;height:65px;z-index:2"></div>

<!-- MISSION -->
<section class="mission">
  <div class="photo" style="left:560px;top:0;width:640px;height:604px;background:linear-gradient(90deg,#eef0ee 0%,#a9b9c4 35%,#7f9f78 70%,#c8d8b8 100%)" role="img" aria-label="Laughing senior couple outdoors, the woman hugging the man from behind"></div>
  <div class="abs" style="left:106px;top:329px;width:8px;height:134px;background:var(--navy)"></div>
  <div class="abs" style="left:106px;top:455px;width:158px;height:8px;background:var(--navy)"></div>
  <div class="abs mission-box">
    <h2 class="abs serif" style="left:49px;top:40px">OUR MISSION</h2>
    <div class="underline" style="left:51px;top:87px;width:60px;height:3px"></div>
    <p class="abs mission-text" style="left:51px;top:110px;width:420px">Lorem ipsum dolor sit amet, consectetur adipiscing elit, sed do eiusmod tempor incididunt ut labore et dolore magna aliqua Quis ipsum suspendisse<br>Altrices gravida Risus commodo viverra maecenas ac-cumsan lacus vel facilisis. Lorem ipsum dolor sit amet, consectetur adipiscing elit sed do</p>
  </div>
</section>

<!-- TEAM -->
<section class="team">
  <div class="abs eyebrow" style="left:132px;top:72px;color:#2e2e3e">OUR TEAM</div>
  <h2 class="abs serif" style="left:130px;top:97px;font-size:40px">MEET THE TEAM</h2>
  <div class="underline" style="left:132px;top:152px;width:60px"></div>
  <p class="abs" style="left:554px;top:74px;width:520px;font-size:16px;line-height:22px">Lorem ipsum dolor sit amet, consectetur adipiscing elit, sed do eiusmod tempor incididunt ut labore etLorem ipsum dolor sit amet, consectetur adipiscing</p>

  <div class="member" style="left:126px;top:216px">
    <div class="photo" style="background:linear-gradient(180deg,#4a4a4e,#6b6d74)" role="img" aria-label="Portrait of a smiling man in glasses and a blue shirt"></div>
    <div class="frame"></div><div class="name">Member Name</div>
  </div>
  <div class="member active" style="left:461px;top:216px">
    <div class="photo" role="img" aria-label="Portrait of a team member, shown with details overlay"></div>
    <div class="overlay">
      <h4>Member Name</h4>
      <p>Lorem ipsum dolor sit amet, con-sectetur adipiscing elit, sed do eiusmod tempor incididunt ut labore et dolore magna aliqua. Quis ipsum suspendiss</p>
      <a>READ MORE</a>
    </div>
  </div>
  <div class="member" style="left:788px;top:216px">
    <div class="photo" style="background:linear-gradient(180deg,#f2f2f2,#d8d8da)" role="img" aria-label="Portrait of a smiling man in a dark suit"></div>
    <div class="frame" style="border-color:rgba(0,0,0,.12)"></div><div class="name">Member Name</div>
  </div>
  <div class="member" style="left:126px;top:565px">
    <div class="photo" style="background:linear-gradient(180deg,#e8e8ea,#b9b4ae)" role="img" aria-label="Portrait of a smiling woman with long hair in a dark blazer"></div>
    <div class="frame"></div><div class="name">Member Name</div>
  </div>
  <div class="member" style="left:459px;top:567px">
    <div class="photo" style="background:linear-gradient(180deg,#8c8c90,#6e7f98)" role="img" aria-label="Portrait of a smiling man in glasses with arms crossed"></div>
    <div class="frame"></div><div class="name">Member Name</div>
  </div>
  <div class="member" style="left:789px;top:567px">
    <div class="photo" style="background:linear-gradient(180deg,#f4f4f4,#dcdcde)" role="img" aria-label="Portrait of a woman with dark hair in a white blouse"></div>
    <div class="frame" style="border-color:rgba(0,0,0,.12)"></div><div class="name">Member Name</div>
  </div>
</section>

<!-- CONTACT -->
<section class="contact">
  <div class="photo" style="left:560px;top:0;width:640px;height:620px;background:linear-gradient(90deg,rgba(205,205,208,0) 0%,#d8cfc4 30%,#c7b29d 60%,#9ea8b5 100%)" role="img" aria-label="Couple reviewing paperwork with an advisor at a bright table"></div>
  <div class="abs eyebrow" style="left:124px;top:112px;color:var(--white)">CONTACT US</div>
  <h2 class="abs serif" style="left:122px;top:134px;color:var(--white)">GET STARTED NOW</h2>
  <div class="field" style="left:126px;top:213px;width:229px;height:43px">
    <svg width="16" height="16" viewBox="0 0 16 16" fill="none" stroke="#888" stroke-width="1.3"><circle cx="8" cy="5" r="3"/><path d="M2 15a6 6 0 0 1 12 0"/></svg>First Name</div>
  <div class="field" style="left:370px;top:213px;width:228px;height:43px">
    <svg width="16" height="16" viewBox="0 0 16 16" fill="none" stroke="#888" stroke-width="1.3"><circle cx="8" cy="5" r="3"/><path d="M2 15a6 6 0 0 1 12 0"/></svg>Last Name</div>
  <div class="field" style="left:126px;top:273px;width:229px;height:42px">
    <svg width="16" height="14" viewBox="0 0 16 14" fill="none" stroke="#888" stroke-width="1.3"><rect x="1" y="2" width="14" height="10"/><path d="M1 2l7 6 7-6"/></svg>Email address</div>
  <div class="field" style="left:370px;top:273px;width:228px;height:42px">
    <svg width="16" height="16" viewBox="0 0 16 16" fill="none" stroke="#888" stroke-width="1.3"><path d="M3 2h3l1 3-2 1a8 8 0 0 0 5 5l1-2 3 1v3C8 14 2 8 3 2z"/></svg>Phone</div>
  <div class="field area" style="left:126px;top:330px;width:472px;height:112px">Message</div>
  <div class="btn navy" style="left:126px;top:459px;width:188px;height:46px;font-size:15px;gap:12px">
    <svg width="30" height="36" viewBox="0 0 32 36"><path d="M3 3l22 15L3 33M10 10l12 8-12 8" fill="none" stroke="#fff" stroke-width="2"/></svg>
    SEND MESSAGE
  </div>
  <svg class="abs" style="left:0;top:0" width="1200" height="659" viewBox="0 0 1200 659">
    <polygon points="630,640 1200,550 1200,659 630,659" fill="#28285c"/>
    <polygon points="0,659 0,636 1200,610 1200,659" fill="#ffffff"/>
  </svg>
</section>

<!-- FOOTER -->
<footer class="footer">
  <div class="logo" style="left:112px;top:86px;width:270px">
    <div style="font-size:21px">CRESTLINE WEALTH</div>
    <div style="font-size:17px;letter-spacing:4px">MANAGEMENT</div>
  </div>
  <div class="social" style="left:190px;top:182px"></div>
  <div class="social" style="left:225px;top:182px"></div>
  <div class="social" style="left:260px;top:182px"></div>

  <h4 style="left:431px;top:30px">NAVIGATION</h4>
  <ul style="left:433px;top:82px"><li>Home</li><li>About Us</li><li>Our Mission</li><li>Services</li></ul>
  <h4 style="left:621px;top:30px">RESOURCES</h4>
  <ul style="left:623px;top:84px"><li>Blogs</li><li>Our Team</li><li>Contact Us</li></ul>
  <h4 style="left:840px;top:30px">CONTACT US</h4>
  <div class="fcontact" style="left:843px;top:84px">
    <span class="icon-dot"><svg width="12" height="14" viewBox="0 0 12 14"><path d="M6 1a4 4 0 0 0-4 4c0 3 4 8 4 8s4-5 4-8a4 4 0 0 0-4-4z" fill="#fff"/></svg></span>
    <span>27 Harbor Lane,<br>Fairview, NY</span></div>
  <div class="fcontact" style="left:843px;top:138px;align-items:center">
    <span class="icon-dot"><svg width="12" height="12" viewBox="0 0 12 12"><path d="M2 1h3l1 3-2 1a6 6 0 0 0 3 3l1-2 3 1v3C5 11 1 7 2 1z" fill="#fff"/></svg></span>
    <span>(+123) 555 0148</span></div>
  <div class="fcontact" style="left:843px;top:180px;align-items:center">
    <span class="icon-dot"><svg width="13" height="10" viewBox="0 0 13 10"><rect x="0" y="0" width="13" height="10" fill="#fff"/><path d="M0 0l6.5 5L13 0" fill="none" stroke="#28285c" stroke-width="1.2"/></svg></span>
    <span>enquiry@crestlinewealth.com</span></div>

  <div class="divider" style="left:106px;top:288px;width:1014px;background:#c4c4c8"></div>
  <p class="copyright">Copyright 2024 <u>Crestline Wealth Management</u>. All Right Reserved</p>
</footer>

</body>
</html>
```